Football blog needs a Wordpress design new site

We need a wordpress design for a new football blog site. We would like to see a design that uses the colours green, white and black and one that makes good use of the slideshow widgets as scene in the site 'www.trenvix.net'
We would like a modern and sleek looking site but one that is also professional and easy to navigate.
Unfortunately due to unforeseen circumstances we are having to shorten the deadline date for this project.
The new deadline date is 16/07/2014.
We apologise for any inconveniance
It Professional

```html
<!DOCTYPE html>
<html lang="en">
<head>
<meta charset="utf-8">
<title>Sideline Chatter – Football Blog</title>
<link rel="stylesheet" href="https://fonts.googleapis.com/css2?family=PT+Sans:wght@400;700&display=swap">
<style>
:root{
  --green:#3ddc4a;
  --green-dark:#2f9e2a;
  --grass-a:#3f8a1f;
  --grass-b:#5aa52c;
  --black:#0b0b0b;
  --panel:#141414;
  --white:#ffffff;
  --text:#444444;
  --muted:#666666;
  --line:#dddddd;
}
*{box-sizing:border-box;margin:0;padding:0}
html,body{width:814px;height:1200px;overflow:hidden}
body{font-family:"PT Sans",Arial,sans-serif;background:var(--white);color:var(--text);position:relative;font-size:8px;line-height:1.35}
a{color:inherit;text-decoration:none}
.abs{position:absolute}

/* header */
.site-header{position:absolute;left:0;top:0;width:814px;height:105px;background:var(--white);border-bottom:3px solid var(--green)}
.brand{position:absolute;left:120px;top:28px;display:flex;align-items:center;gap:8px}
.brand-dot{width:30px;height:30px;border-radius:50%;background:var(--green)}
.brand-name{font-size:34px;font-weight:700;color:var(--black);letter-spacing:-1px}
.user-links{position:absolute;right:118px;top:12px;display:flex;gap:6px;align-items:center;font-size:8px;color:var(--muted)}
.social-dot{width:9px;height:9px;border-radius:50%;background:#555;display:inline-block}
.main-nav{position:absolute;right:116px;top:44px;display:flex;gap:13px;font-size:8.5px;color:#555}
.search{position:absolute;left:502px;top:71px;width:195px;height:22px;display:flex}
.search-input{flex:1;background:#efefef;border:1px solid #e2e2e2;font-size:8px;color:#666;padding:6px 8px}
.search-btn{width:22px;background:var(--green-dark);display:flex;align-items:center;justify-content:center}

/* grass */
.pitch{position:absolute;left:0;top:108px;width:814px;height:891px;background:linear-gradient(90deg,var(--grass-a),var(--grass-b) 50%,var(--grass-a));border-bottom:3px solid var(--green)}

.primary-nav{position:absolute;left:116px;top:116px;width:582px;height:33px;background:linear-gradient(#2a2a2a,#0d0d0d);display:flex;align-items:center;gap:36px;padding-left:19px;font-size:8.5px;color:var(--white)}
.primary-nav .active{color:var(--green)}

/* slider */
.slider{position:absolute;left:116px;top:151px;width:582px;height:268px;background:var(--black)}
.slide-main{position:absolute;left:2px;top:3px;width:373px;height:210px;background:linear-gradient(160deg,#c9c9c9,#8b8f86 45%,#6f8a3f)}
.slide-caption{position:absolute;left:2px;top:215px;width:373px;height:50px;background:#1b1b1b;color:var(--white);padding:7px 56px 0 8px}
.slide-caption h2{font-size:10px;font-weight:700;margin-bottom:3px}
.slide-caption p{font-size:6.8px;line-height:1.4}
.more-btn{position:absolute;left:328px;top:4px;width:44px;height:42px;background:var(--green);color:var(--white);font-size:13px;display:flex;align-items:center;justify-content:center}
.slide-list{position:absolute;left:381px;top:3px;width:199px}
.slide-item{height:64px;margin-bottom:3px;background:#1b1b1b;display:flex;border-left:1px solid #333}
.slide-item .txt{width:104px;padding:6px 0 0 9px;color:var(--white)}
.date{color:var(--green);font-size:7px}
.slide-item h3{font-size:7px;font-weight:700;margin:2px 0}
.slide-item p{font-size:6.8px}
.thumb{flex:1;margin:1px 1px 1px 0}

/* must read */
.must-read{position:absolute;left:116px;top:425px;width:582px;height:211px;background:var(--white);padding:10px 11px}
.section-title{font-size:17px;color:#222;font-weight:400}
.cards{display:flex;gap:10px;margin-top:6px}
.card{width:133px}
.card .photo{height:93px;border:2px solid #e6e6e6}
.card .date{display:block;margin-top:8px}
.card h3{font-size:7px;font-weight:700;color:#222;margin:3px 0}
.card p{font-size:6.8px;color:var(--muted)}
.read-more{color:var(--green-dark);font-size:7px}

/* posts area */
.posts{position:absolute;left:116px;top:643px;width:582px;height:347px;background:var(--black)}
.post{position:absolute;left:6px;width:322px;height:100px;background:var(--white);display:flex;padding:7px}
.post .photo{width:96px;height:86px}
.post .body{padding-left:13px}
.post h3{font-size:9.5px;color:#333;font-weight:700}
.post .meta{font-size:7px;color:#555;margin:2px 0 7px}
.post p{font-size:6.8px;color:var(--muted)}
.sidebar{position:absolute;left:345px;top:8px;width:229px;color:var(--white)}
.sidebar .section-title{color:var(--white)}
.news{margin-top:6px}
.news .meta{color:var(--green);font-size:7px}
.news p{font-size:6.5px;margin:3px 0 10px}
.sidebar .divider{border-top:1px solid #333;margin:4px 0 10px}
.articles{list-style:none;margin-top:8px}
.articles li{font-size:7px;margin-bottom:13px;display:flex;gap:6px;align-items:center}
.articles li.current{color:var(--green)}

/* footer */
.site-footer{position:absolute;left:116px;top:1008px;width:582px}
.footer-col{position:absolute;top:10px}
.footer-title{font-size:13px;color:#444}
.fpost{display:flex;gap:6px;margin-top:9px}
.fpost .photo{width:56px;height:43px;border:2px solid #333}
.fpost h3{font-size:9px;color:#333;font-weight:700}
.fpost p{font-size:6.5px;color:#555;margin-top:2px}
.about p{font-size:7px;color:#555;margin:8px 0 12px}
.social{display:flex;gap:10px;margin-top:10px}
.social span{width:14px;height:14px;border-radius:50%;background:#999}
.footer-bar{position:absolute;left:116px;top:1154px;width:582px;border-top:2px solid var(--green);padding-top:10px;display:flex;justify-content:space-between}
.footer-brand{display:flex;gap:5px;align-items:center}
.footer-brand .brand-dot{width:14px;height:14px}
.footer-brand b{font-size:11px;color:var(--black)}
.footer-brand small{display:block;font-size:7px;color:#555}
.footer-nav{display:flex;gap:12px;font-size:8px;color:#444;padding-top:8px}
</style>
</head>
<body>

<header class="site-header">
  <a class="brand" href="#"><span class="brand-dot"></span><span class="brand-name">Sideline Chatter</span></a>
  <div class="user-links">
    <span>New User?</span><a href="#">Register</a><a href="#">Login</a><a href="#">Help</a>
    <span class="social-dot" aria-label="Social network"></span><span class="social-dot" aria-label="Social network"></span><span class="social-dot" aria-label="Social network"></span><span class="social-dot" aria-label="Social network"></span>
  </div>
  <nav class="main-nav"><a>NEWS</a><a>RACES</a><a>RESULTS</a><a>GALLERY</a><a>VIDEO</a><a>TEAMS &amp; COACHES</a></nav>
  <div class="search">
    <div class="search-input">Search...</div>
    <div class="search-btn"><svg width="12" height="12" viewBox="0 0 12 12"><circle cx="5" cy="5" r="3.5" fill="none" stroke="#fff" stroke-width="1.5"/><line x1="7.5" y1="7.5" x2="11" y2="11" stroke="#fff" stroke-width="1.8"/></svg></div>
  </div>
</header>

<div class="pitch" role="img" aria-label="Grass pitch background"></div>

<nav class="primary-nav"><a class="active">HOME</a><a>OUR FORUM</a><a>NEWS</a><a>BLOGS</a><a>SOLUTIONS</a><a>ADVANCED SEARCH</a></nav>

<section class="slider">
  <div class="slide-main" role="img" aria-label="Goalkeeper diving for a save in a stadium"></div>
  <div class="slide-caption">
    <h2>Curabitur venenatis nisi scelerisque, consectetur nisi euismod,</h2>
    <p>Sed laoreet viverra tortor, vitae lacinia turpis consequat sit amet. Donec faucibus, leo vel ulla-mcorper cursus, arcu massa ultrices mi, non viverra sapien tellus et mi. Phasellus tempor ut</p>
    <a class="more-btn" href="#">More</a>
  </div>
  <div class="slide-list">
    <div class="slide-item"><div class="txt"><span class="date">July 28,2014</span><h3>ELIPPORY TENDORRETY</h3><p>Proin bibendum, velit eu venenatis aliquam, massa</p></div><div class="thumb" role="img" aria-label="Goalkeeper save" style="background:linear-gradient(#bfc4c0,#5f8a3a)"></div></div>
    <div class="slide-item"><div class="txt"><span class="date">July 28,2014</span><h3>ELIPPORY TENDORRETY</h3><p>Proin bibendum, velit eu venenatis aliquam, massa</p></div><div class="thumb" role="img" aria-label="Ball on the pitch" style="background:linear-gradient(#9aa35a,#4c7d25)"></div></div>
    <div class="slide-item"><div class="txt"><span class="date">July 28,2014</span><h3>ELIPPORY TENDORRETY</h3><p>Proin bibendum, velit eu venenatis aliquam, massa</p></div><div class="thumb" role="img" aria-label="Player celebrating" style="background:linear-gradient(#2d3a22,#4f8a2a)"></div></div>
    <div class="slide-item"><div class="txt"><span class="date">July 28,2014</span><h3>ELIPPORY TENDORRETY</h3><p>Proin bibendum, velit eu venenatis aliquam, massa</p></div><div class="thumb" role="img" aria-label="Players in a match" style="background:linear-gradient(#7b8e9c,#5a9a3a)"></div></div>
  </div>
</section>

<section class="must-read">
  <h2 class="section-title">Must Read</h2>
  <div class="cards">
    <article class="card"><div class="photo" role="img" aria-label="Player sliding on grass" style="background:linear-gradient(#c8cfc6,#6f9b4a)"></div><span class="date">July 28,2014</span><h3>ELIPPORY TENDORRETY</h3><p>Proin bibendum, velit eu vene dfnatis aliquam, massa lorem sagittis ipsum,</p><a class="read-more">Read More</a></article>
    <article class="card"><div class="photo" role="img" aria-label="Player in yellow kit on the pitch" style="background:linear-gradient(#d7c94a,#4f8f2a)"></div><span class="date">July 28,2014</span><h3>ELIPPORY TENDORRETY</h3><p>Proin bibendum, velit eu vene dfnatis aliquam, massa lorem sagittis ipsum,</p><a class="read-more">Read More</a></article>
    <article class="card"><div class="photo" role="img" aria-label="Player kicking the ball" style="background:linear-gradient(#c9c0bc,#5d8c36)"></div><span class="date">July 28,2014</span><h3>ELIPPORY TENDORRETY</h3><p>Proin bibendum, velit eu vene dfnatis aliquam, massa lorem sagittis ipsum,</p><a class="read-more">Read More</a></article>
    <article class="card"><div class="photo" role="img" aria-label="Player in red kit running" style="background:linear-gradient(#b84a3a,#4c8a2a)"></div><span class="date">July 28,2014</span><h3>ELIPPORY TENDORRETY</h3><p>Proin bibendum, velit eu vene dfnatis aliquam, massa lorem sagittis ipsum,</p><a class="read-more">Read More</a></article>
  </div>
</section>

<section class="posts">
  <article class="post" style="top:11px"><div class="photo" role="img" aria-label="Fans with flares in the stands" style="background:linear-gradient(#2a1a1a,#b63a3a)"></div><div class="body"><h3>Proin metus magna, pharetra</h3><div class="meta">July 28, 2014 | 5 Comments | By Admin</div><p>Curabitur viverra neque nec urna blandit vulputate. Sed fringilla pellentesque nisl non iaculis. Vestibulum ante ipsum primis in faucibus orci luctus et ultrices posuere cubilia Curae; In vel vehicula quam. Pellentesque sodales</p><a class="read-more">Read More</a></div></article>
  <article class="post" style="top:123px"><div class="photo" role="img" aria-label="Supporters cheering" style="background:linear-gradient(#1f3a6a,#6f8fb0)"></div><div class="body"><h3>Proin metus magna, pharetra</h3><div class="meta">July 28, 2014 | 5 Comments | By Admin</div><p>Curabitur viverra neque nec urna blandit vulputate. Sed fringilla pellentesque nisl non iaculis. Vestibulum ante ipsum primis in faucibus orci luctus et ultrices posuere cubilia Curae; In vel vehicula quam. Pellentesque sodales</p><a class="read-more">Read More</a></div></article>
  <article class="post" style="top:235px"><div class="photo" role="img" aria-label="Boot resting on a ball" style="background:linear-gradient(#e6efe0,#4f9a2a)"></div><div class="body"><h3>Proin metus magna, pharetra</h3><div class="meta">July 28, 2014 | 5 Comments | By Admin</div><p>Curabitur viverra neque nec urna blandit vulputate. Sed fringilla pellentesque nisl non iaculis. Vestibulum ante ipsum primis in faucibus orci luctus et ultrices posuere cubilia Curae; In vel vehicula quam. Pellentesque sodales</p><a class="read-more">Read More</a></div></article>

  <aside class="sidebar">
    <h2 class="section-title">Recent News</h2>
    <div class="news">
      <div class="meta">July 28, 2014 | 5 COMMENTS | By Admin</div><p>Nulla varius lacus nisi, ut tincidunt odio suscipit quis. Nulla facilisi. Nullam lacinia quis turpis et dignissim. Cras iaculis aliquam mauris, eu imperdiet dui venenatis ut.</p>
      <div class="meta">July 28, 2014 | 5 COMMENTS | By Admin</div><p>Nulla varius lacus nisi, ut tincidunt odio suscipit quis. Nulla facilisi. Nullam lacinia quis turpis et dignissim. Cras iaculis aliquam mauris, eu imperdiet dui venenatis ut.</p>
      <div class="meta">July 28, 2014 | 5 COMMENTS | By Admin</div><p>Nulla varius lacus nisi, ut tincidunt odio suscipit quis. Nulla facilisi. Nullam lacinia quis turpis et dignissim. Cras iaculis aliquam mauris, eu imperdiet dui venenatis ut.</p>
    </div>
    <div class="divider"></div>
    <h2 class="section-title">Recent Articles</h2>
    <ul class="articles">
      <li class="current"><svg width="7" height="6" viewBox="0 0 7 6"><path d="M0 3h5M3 0.5L6 3 3 5.5" stroke="currentColor" fill="none" stroke-width="1.2"/></svg>Cras hendrerit porttitor nisi vitae pellentesque. Pellentesque in</li>
      <li><svg width="7" height="6" viewBox="0 0 7 6"><path d="M0 3h5M3 0.5L6 3 3 5.5" stroke="currentColor" fill="none" stroke-width="1.2"/></svg>Posuere est, ac placerat augue. Curabitur ullamcorper purus a</li>
      <li><svg width="7" height="6" viewBox="0 0 7 6"><path d="M0 3h5M3 0.5L6 3 3 5.5" stroke="currentColor" fill="none" stroke-width="1.2"/></svg>Orci consectetur faucibus. Phasellus pretium ante in mi tincid-</li>
      <li><svg width="7" height="6" viewBox="0 0 7 6"><path d="M0 3h5M3 0.5L6 3 3 5.5" stroke="currentColor" fill="none" stroke-width="1.2"/></svg>Unt, at malesuada neque venenatis. Cras scelerisque, sem non</li>
      <li><svg width="7" height="6" viewBox="0 0 7 6"><path d="M0 3h5M3 0.5L6 3 3 5.5" stroke="currentColor" fill="none" stroke-width="1.2"/></svg>Wccumsan commodo, urna ipsum imperdiet arcu, eget euis-</li>
    </ul>
  </aside>
</section>

<footer>
  <div class="site-footer">
    <div class="footer-col" style="left:2px;width:260px">
      <h2 class="footer-title">Recent Post</h2>
      <div class="fpost"><div class="photo" role="img" aria-label="Stadium view" style="background:linear-gradient(#8aa0b4,#4f8a2a)"></div><div><h3>Proin metus magna, pharetra</h3><p>Nulla varius lacus nisi, ut tincidunt odio suscipit quis. Nulla facilisi. Nullam lacinia quis turpis et dignissim. Cras iaculis aliquam mauris,</p></div></div>
      <div class="fpost"><div class="photo" role="img" aria-label="Match action at goal" style="background:linear-gradient(#3a4a5a,#5a9a3a)"></div><div><h3>Proin metus magna, pharetra</h3><p>Nulla varius lacus nisi, ut tincidunt odio suscipit quis. Nulla facilisi. Nullam lacinia quis turpis et dignissim. Cras iaculis aliquam mauris,</p></div></div>
    </div>
    <div class="footer-col about" style="left:344px;width:238px">
      <h2 class="footer-title">About Sideline Chatter</h2>
      <p>Lorem ipsum dolor sit amet, consectetur adipiscing elit. Ut porttitor elit justo, quis varius enim egestas id. Cras eget venenatis dui. Sed vel lectus augue. Maecenas eleifend elementum aliquam. Fusce eu lectus adipiscing, mattis dolor tempus, dictum massa.</p>
      <h2 class="footer-title">Social Media</h2>
      <div class="social"><span aria-label="Social network"></span><span aria-label="Social network"></span><span aria-label="Social network"></span><span aria-label="Social network"></span></div>
    </div>
  </div>
  <div class="footer-bar">
    <div class="footer-brand"><span class="brand-dot"></span><div><b>Sideline Chatter</b><small>© 2014 Privacy Policy</small></div></div>
    <nav class="footer-nav"><a>HOME</a><a>OUR FORUM</a><a>NEWS</a><a>BLOGS</a><a>SOLUTIONS</a><a>ADVANCED SEARCH</a></nav>
  </div>
</footer>

</body>
</html>
```